Verdanix Medical Business Card

Create a high class Business card for Medical Aesthetics and Wellness Practice called Verdanix Medical Aesthetics and Wellness as per the logo attached.
Addresss is: 418 Harlan Brook Road Suite 312 Melville, New York 11093
Phone (555)204-7391 IG @verdanix_medical
Verdanixmedical.example

I need 5 different name configurations
1) Dr. Theo Valcourt
Aesthetics and Wellness Specialist
Medical Director

2) Rosalind Pettinger, NP
Clinical Nurse Manager

3) Marla Vostrik, RN
Aesthetic Nurse Specialist

4) Petra Halvesen, RN

5) Dana Kowbeck, L.E.
Senior Licensed Esthetician

Target Market(s)

22-55 Females

Industry/Entity Type

Medical Spa and Wellness

Contact Information for Business Card

Logo, address, phone, web, instagram, providers name

Requirements
Must have
• Attractive classy modern look

```html
<!DOCTYPE html>
<html lang="en">
<head>
<meta charset="utf-8">
<title>Verdanix Medical Business Cards</title>
<link rel="stylesheet" href="https://fonts.googleapis.com/css2?family=Source+Serif+4:wght@400;600&display=swap">
<style>
  :root {
    --stage: #3a3a3a;
    --stage-dark: #1c1c1c;
    --card-white: #ffffff;
    --card-black: #050505;
    --ink: #1e1e1e;
    --ink-soft: #4a4a4a;
    --silver: #d2d2d2;
    --silver-dim: #a0a0a0;
  }
  * { margin: 0; padding: 0; box-sizing: border-box; }
  html, body { width: 1200px; height: 4370px; overflow: hidden; }
  body {
    background: linear-gradient(180deg, var(--stage) 0%, var(--stage-dark) 100%);
    font-family: "Source Serif 4", Georgia, serif;
    -webkit-font-smoothing: antialiased;
    -moz-osx-font-smoothing: grayscale;
  }
  .card-set {
    height: 874px;
    display: flex;
    align-items: center;
    justify-content: center;
    gap: 60px;
    border-bottom: 1px solid #151515;
  }
  .card {
    width: 520px;
    height: 300px;
    border-radius: 22px;
    box-shadow: 0 24px 50px rgba(0,0,0,0.55);
  }
  .card-front {
    background: var(--card-white);
    display: flex;
    flex-direction: column;
    align-items: center;
    justify-content: center;
    color: var(--ink);
  }
  .brand-name {
    font-family: "Source Serif 4", Georgia, serif;
    font-weight: 400;
    font-size: 56px;
    letter-spacing: 5px;
    line-height: 1;
    color: var(--ink);
  }
  .brand-tagline {
    margin-top: 12px;
    font-size: 15px;
    font-weight: 400;
    letter-spacing: 1.2px;
    text-transform: uppercase;
    color: var(--ink);
  }
  .brand-city {
    margin-top: 6px;
    font-size: 10px;
    letter-spacing: 6px;
    text-transform: uppercase;
    color: var(--ink-soft);
  }
  .card-back {
    background: var(--card-black);
    display: flex;
    align-items: center;
    justify-content: center;
    padding: 0 28px;
    color: var(--silver);
  }
  .provider {
    text-align: right;
    padding-right: 16px;
    flex: 0 0 auto;
  }
  .provider-name {
    font-size: 17px;
    font-weight: 600;
    letter-spacing: 0.6px;
    text-transform: uppercase;
    color: var(--silver);
  }
  .provider-role {
    margin-top: 2px;
    font-size: 11.5px;
    line-height: 1.35;
    color: var(--silver-dim);
  }
  .divider {
    width: 1px;
    height: 96px;
    background: var(--silver-dim);
    flex: 0 0 auto;
  }
  .contact-list {
    list-style: none;
    padding-left: 16px;
    font-size: 11.5px;
    line-height: 1.45;
    color: var(--silver);
  }
  .contact-list li { display: flex; align-items: flex-start; gap: 8px; white-space: nowrap; }
  .contact-list svg { width: 10px; height: 10px; margin-top: 4px; flex: 0 0 auto; fill: var(--silver); }
</style>
</head>
<body>

<section class="card-set">
  <div class="card card-front">
    <div class="brand-name">verdanix</div>
    <div class="brand-tagline">Medical Aesthetics and Wellness</div>
    <div class="brand-city">New York</div>
  </div>
  <div class="card card-back">
    <div class="provider">
      <div class="provider-name">Dr. Theo Valcourt</div>
      <div class="provider-role">Aesthetics &amp; Wellness Specialist<br>Medical Director</div>
    </div>
    <div class="divider"></div>
    <ul class="contact-list">
      <li><svg viewBox="0 0 10 10"><path d="M5 0a3.5 3.5 0 0 0-3.5 3.5C1.5 6 5 10 5 10s3.5-4 3.5-6.5A3.5 3.5 0 0 0 5 0zm0 5a1.5 1.5 0 1 1 0-3 1.5 1.5 0 0 1 0 3z"/></svg><span>418 Harlan Brook Road<br>Suite 312 Melville, NY 11093</span></li>
      <li><svg viewBox="0 0 10 10"><path d="M2 0.5l2 2-1 1.2a6 6 0 0 0 3.3 3.3l1.2-1 2 2-1.2 1.5C4.5 9.5 0.5 5.5 0.5 1.7z"/></svg><span>(555)204-7391</span></li>
      <li><svg viewBox="0 0 10 10"><circle cx="5" cy="5" r="4"/></svg><span>@verdanix_medical</span></li>
      <li><svg viewBox="0 0 10 10"><path d="M5 0.5a4.5 4.5 0 1 0 0 9 4.5 4.5 0 0 0 0-9zm0 1c.6.7 1 1.9 1.1 3H3.9C4 3.4 4.4 2.2 5 1.5zM3.9 5.5h2.2C6 6.6 5.6 7.8 5 8.5c-.6-.7-1-1.9-1.1-3z"/></svg><span>Verdanixmedical.example</span></li>
    </ul>
  </div>
</section>

<section class="card-set">
  <div class="card card-front">
    <div class="brand-name">verdanix</div>
    <div class="brand-tagline">Medical Aesthetics and Wellness</div>
    <div class="brand-city">New York</div>
  </div>
  <div class="card card-back">
    <div class="provider">
      <div class="provider-name">Rosalind Pettinger, NP</div>
      <div class="provider-role">Clinical Nurse Manager</div>
    </div>
    <div class="divider"></div>
    <ul class="contact-list">
      <li><svg viewBox="0 0 10 10"><path d="M5 0a3.5 3.5 0 0 0-3.5 3.5C1.5 6 5 10 5 10s3.5-4 3.5-6.5A3.5 3.5 0 0 0 5 0zm0 5a1.5 1.5 0 1 1 0-3 1.5 1.5 0 0 1 0 3z"/></svg><span>418 Harlan Brook Road<br>Suite 312 Melville, NY 11093</span></li>
      <li><svg viewBox="0 0 10 10"><path d="M2 0.5l2 2-1 1.2a6 6 0 0 0 3.3 3.3l1.2-1 2 2-1.2 1.5C4.5 9.5 0.5 5.5 0.5 1.7z"/></svg><span>(555)204-7391</span></li>
      <li><svg viewBox="0 0 10 10"><circle cx="5" cy="5" r="4"/></svg><span>@verdanix_medical</span></li>
      <li><svg viewBox="0 0 10 10"><path d="M5 0.5a4.5 4.5 0 1 0 0 9 4.5 4.5 0 0 0 0-9zm0 1c.6.7 1 1.9 1.1 3H3.9C4 3.4 4.4 2.2 5 1.5zM3.9 5.5h2.2C6 6.6 5.6 7.8 5 8.5c-.6-.7-1-1.9-1.1-3z"/></svg><span>Verdanixmedical.example</span></li>
    </ul>
  </div>
</section>

<section class="card-set">
  <div class="card card-front">
    <div class="brand-name">verdanix</div>
    <div class="brand-tagline">Medical Aesthetics and Wellness</div>
    <div class="brand-city">New York</div>
  </div>
  <div class="card card-back">
    <div class="provider">
      <div class="provider-name">Marla Vostrik, RN</div>
      <div class="provider-role">Aesthetic Nurse Specialist</div>
    </div>
    <div class="divider"></div>
    <ul class="contact-list">
      <li><svg viewBox="0 0 10 10"><path d="M5 0a3.5 3.5 0 0 0-3.5 3.5C1.5 6 5 10 5 10s3.5-4 3.5-6.5A3.5 3.5 0 0 0 5 0zm0 5a1.5 1.5 0 1 1 0-3 1.5 1.5 0 0 1 0 3z"/></svg><span>418 Harlan Brook Road<br>Suite 312 Melville, NY 11093</span></li>
      <li><svg viewBox="0 0 10 10"><path d="M2 0.5l2 2-1 1.2a6 6 0 0 0 3.3 3.3l1.2-1 2 2-1.2 1.5C4.5 9.5 0.5 5.5 0.5 1.7z"/></svg><span>(555)204-7391</span></li>
      <li><svg viewBox="0 0 10 10"><circle cx="5" cy="5" r="4"/></svg><span>@verdanix_medical</span></li>
      <li><svg viewBox="0 0 10 10"><path d="M5 0.5a4.5 4.5 0 1 0 0 9 4.5 4.5 0 0 0 0-9zm0 1c.6.7 1 1.9 1.1 3H3.9C4 3.4 4.4 2.2 5 1.5zM3.9 5.5h2.2C6 6.6 5.6 7.8 5 8.5c-.6-.7-1-1.9-1.1-3z"/></svg><span>Verdanixmedical.example</span></li>
    </ul>
  </div>
</section>

<section class="card-set">
  <div class="card card-front">
    <div class="brand-name">verdanix</div>
    <div class="brand-tagline">Medical Aesthetics and Wellness</div>
    <div class="brand-city">New York</div>
  </div>
  <div class="card card-back">
    <div class="provider">
      <div class="provider-name">Petra Halvesen, RN</div>
      <div class="provider-role">Aesthetic Nurse Specialist</div>
    </div>
    <div class="divider"></div>
    <ul class="contact-list">
      <li><svg viewBox="0 0 10 10"><path d="M5 0a3.5 3.5 0 0 0-3.5 3.5C1.5 6 5 10 5 10s3.5-4 3.5-6.5A3.5 3.5 0 0 0 5 0zm0 5a1.5 1.5 0 1 1 0-3 1.5 1.5 0 0 1 0 3z"/></svg><span>418 Harlan Brook Road<br>Suite 312 Melville, NY 11093</span></li>
      <li><svg viewBox="0 0 10 10"><path d="M2 0.5l2 2-1 1.2a6 6 0 0 0 3.3 3.3l1.2-1 2 2-1.2 1.5C4.5 9.5 0.5 5.5 0.5 1.7z"/></svg><span>(555)204-7391</span></li>
      <li><svg viewBox="0 0 10 10"><circle cx="5" cy="5" r="4"/></svg><span>@verdanix_medical</span></li>
      <li><svg viewBox="0 0 10 10"><path d="M5 0.5a4.5 4.5 0 1 0 0 9 4.5 4.5 0 0 0 0-9zm0 1c.6.7 1 1.9 1.1 3H3.9C4 3.4 4.4 2.2 5 1.5zM3.9 5.5h2.2C6 6.6 5.6 7.8 5 8.5c-.6-.7-1-1.9-1.1-3z"/></svg><span>Verdanixmedical.example</span></li>
    </ul>
  </div>
</section>

<section class="card-set">
  <div class="card card-front">
    <div class="brand-name">verdanix</div>
    <div class="brand-tagline">Medical Aesthetics and Wellness</div>
    <div class="brand-city">New York</div>
  </div>
  <div class="card card-back">
    <div class="provider">
      <div class="provider-name">Dana Kowbeck, L.E.</div>
      <div class="provider-role">Senior Licensed Esthetician</div>
    </div>
    <div class="divider"></div>
    <ul class="contact-list">
      <li><svg viewBox="0 0 10 10"><path d="M5 0a3.5 3.5 0 0 0-3.5 3.5C1.5 6 5 10 5 10s3.5-4 3.5-6.5A3.5 3.5 0 0 0 5 0zm0 5a1.5 1.5 0 1 1 0-3 1.5 1.5 0 0 1 0 3z"/></svg><span>418 Harlan Brook Road<br>Suite 312 Melville, NY 11093</span></li>
      <li><svg viewBox="0 0 10 10"><path d="M2 0.5l2 2-1 1.2a6 6 0 0 0 3.3 3.3l1.2-1 2 2-1.2 1.5C4.5 9.5 0.5 5.5 0.5 1.7z"/></svg><span>(555)204-7391</span></li>
      <li><svg viewBox="0 0 10 10"><circle cx="5" cy="5" r="4"/></svg><span>@verdanix_medical</span></li>
      <li><svg viewBox="0 0 10 10"><path d="M5 0.5a4.5 4.5 0 1 0 0 9 4.5 4.5 0 0 0 0-9zm0 1c.6.7 1 1.9 1.1 3H3.9C4 3.4 4.4 2.2 5 1.5zM3.9 5.5h2.2C6 6.6 5.6 7.8 5 8.5c-.6-.7-1-1.9-1.1-3z"/></svg><span>Verdanixmedical.example</span></li>
    </ul>
  </div>
</section>

</body>
</html>
```